Tourism Marketing needing sleek, clear design for business card & proposal documents.

***Company background***
"Quiet Harbour" is a company specializing in tourism marketing and project management. We do international wholesale, event management as well as ongoing representation of tourism and hospitality companies.

***Target market***
We cater to tourism companies and hotel professionals.

***Task***
We would like to get a single sided business card designed (but will still consider two sided, we are open to any ideas you may have). The layout for this card should be modern and elegant. Currently we do not have a logo, but we would like our business name in a really simple typography for the business card (similar to Merrow Lounge's logo - www.merrowlounge.com.au).We are after a design that is clear, strong enough to be recognised as Quiet Harbour that does not require any fancy design. Another option is a simple play on QH (Quiet Harbour) or simply have Quiet Harbour featured elsewhere on card more as a brand/logo.

Feel free to submit different fonts if you feel you have any other fonts/designs that may be suitable for this card other than sans serifs. Should this project be successful, we will be considering several other projects for business proposal templates and eventually a website design.

The information that needs to go on the card are as follows:

Odette Farrow
Director
Quiet Harbour
Tourism Marketing & Representation
57 Wendlow Terrace
Prahran, Victoria, 3181 Australia
T +61 428306172 E odette@quietharbour.com.au

***Look and feel***
We'd like the business card design to express the following:
Modern, sleek, elegant, simple, discreet, quality, subtle, professional, creative, innovation

In terms of typography, we like something really simple and blocky (similar font to Merrow Lounge's logo - www.merrowlounge.com.au)

***Colour scheme***
Shades of grey and dark teal

***Note***
Although our main target market are professionals, we would like the business card design to be versatile enough to be used outside of the tourism industry and need to appeal to different markets.

I do not have existing logo. Was hoping for a design that may be clear, strong enough not to require one. Other option is a simple play on QH (Quiet Harbour) or simply have Quiet Harbour featured elsewhere on card more as a brand/logo.

Odette Farrow
Director
Quiet Harbour Pty Ltd 
57 Wendlow Terrace
T +61 428306172  E  odette@quietharbour.com.au

Thank you for designs so far. Many have used a mauve colour which matches our company profile. This is not necessary, as that is just a draft and will be completely redesigned, so dont  feel you need to incorporate the mauve.

My colour preferences are for a white or grey background, and I like fonts in dark teals, grey or other sophisticated but modern colours. feel free to submit different fonts if you you have other fonts you thing would be suitable for this card, along with sans serifs. Should this project be successful, we will be considering several others for business proposal templates and eventually website. 

Target Market(s)

International Hospitality Senior Executives, Directors of International Tourism Companies, Directors of Tourism Bodies Internationally, local Tourism

Industry/Entity Type

Hospitality

Requirements
Should not have
• must not have bright garish colour, swirly patterns or anything that dates too much.

```html
<!DOCTYPE html>
<html lang="en">
<head>
<meta charset="utf-8">
<title>Quiet Harbour — Business Card</title>
<link rel="stylesheet" href="https://fonts.googleapis.com/css2?family=Montserrat:wght@400;500;600;700&display=swap">
<style>
  :root {
    --page: #ffffff;
    --card-grey: #939497;
    --card-white: #ffffff;
    --teal: #1f8f8c;
    --ink-mid: #5f6062;
    --ink-soft: #8b8c8e;
    --on-grey: #ffffff;
    --on-grey-soft: #ececec;
    --shadow: rgba(0, 0, 0, 0.28);
  }
  * { margin: 0; padding: 0; box-sizing: border-box; }
  html, body {
    width: 1200px;
    height: 1200px;
    overflow: hidden;
    background: var(--page);
    font-family: "Montserrat", "Helvetica Neue", Arial, sans-serif;
  }
  .canvas { position: relative; width: 1200px; height: 1200px; }

  .card {
    position: absolute;
    width: 768px;
    height: 470px;
    box-shadow: 6px 8px 10px var(--shadow);
    text-align: center;
  }
  .card--front { left: 215px; top: 88px; background: var(--card-grey); }
  .card--back  { left: 217px; top: 642px; background: var(--card-white); box-shadow: 6px 8px 10px var(--shadow), 0 0 4px rgba(0,0,0,0.06); }

  .wordmark {
    position: absolute;
    left: 0; right: 0;
    top: 190px;
    color: var(--on-grey);
    font-weight: 500;
    font-size: 30px;
    letter-spacing: 0.5em;
    line-height: 1;
  }
  .wordmark__line { display: block; padding-left: 0.5em; }
  .wordmark__rule {
    display: block;
    width: 204px;
    height: 2px;
    margin: 13px auto 14px;
    background: var(--teal);
  }
  .tagline {
    position: absolute;
    left: 0; right: 0;
    top: 402px;
    color: var(--on-grey-soft);
    font-size: 21px;
    letter-spacing: 0.12em;
    font-weight: 400;
  }

  .person {
    position: absolute;
    left: 0; right: 0;
    top: 203px;
  }
  .person__name {
    color: var(--teal);
    font-weight: 700;
    font-size: 24px;
    letter-spacing: 0.12em;
  }
  .person__role {
    margin-top: 4px;
    color: var(--ink-mid);
    font-size: 19px;
    letter-spacing: 0.12em;
  }
  .divider {
    position: absolute;
    left: 282px;
    top: 300px;
    width: 204px;
    height: 2px;
    background: var(--teal);
  }
  .contact {
    position: absolute;
    left: 0; right: 0;
    top: 350px;
    color: var(--ink-soft);
    font-size: 21px;
    letter-spacing: 0.1em;
    line-height: 27px;
  }
  .contact__label {
    color: var(--teal);
    font-weight: 700;
    font-size: 16px;
    margin-right: 4px;
  }
  .contact__gap { display: inline-block; width: 14px; }
</style>
</head>
<body>
<main class="canvas">
  <section class="card card--front" aria-label="Card front">
    <h1 class="wordmark">
      <span class="wordmark__line">QUIET</span>
      <span class="wordmark__rule"></span>
      <span class="wordmark__line">HARBOUR</span>
    </h1>
    <p class="tagline">TOURISM MARKETING &amp; REPRESENTATION</p>
  </section>

  <section class="card card--back" aria-label="Card back">
    <div class="person">
      <p class="person__name">ODETTE FARROW</p>
      <p class="person__role">DIRECTOR</p>
    </div>
    <span class="divider"></span>
    <address class="contact" style="font-style:normal">
      <span>57 WENDLOW TERRACE</span><br>
      <span>PRAHRAN VIC 3181 AUSTRALIA</span><br>
      <span><span class="contact__label">T</span>+61 428 306 172</span><span class="contact__gap"></span><span><span class="contact__label">E</span>odette@quietharbour.com.au</span>
    </address>
  </section>
</main>
</body>
</html>
```